Facial Tissue Brand Logo and Design

We would like you to design a Logo for the Facial Tissue Brand "Velora" along with the box design. The pack should indicate the pack size (150 x 2 ply). Also our company logo should be present (attached) along with a barcode. The box size dimensions should be 210mm (L) x 110mm (W) x 70mm (H). We are open to all kinds of nice designs which are attractive but not overdone. Happy designing!

UPDATE:
We appreciate the designs so far... but would also love to see more options in a simple and elegent design style that would look good on a table... please see attached below links for reference purpose:

www.pixmarrow.com/image-photo/cleaning-wipes-isolated-on-white-480215736

www.pixmarrow.com/image-photo/cleaning-wipes-isolated-on-white-692048153

www.pixmarrow.com/image-photo/delicate-female-hands-pulling-tissue-out-2875013649

Happy desgining!

We appreciate the designs so far.. but would like to to see some more options.

```html
<!DOCTYPE html>
<html lang="en">
<head>
<meta charset="utf-8">
<title>Velora Facial Tissue Box – Flat Panels</title>
<link rel="stylesheet" href="https://fonts.googleapis.com/css2?family=Archivo+Black&family=Arimo:wght@400;700&family=Kaushan+Script&display=swap">
<style>
  :root {
    --bg: #eeeff2;
    --blue-deep: #0567b5;
    --blue-mid: #0a86d2;
    --blue-light: #3aa7e0;
    --navy: #26237e;
    --white: #ffffff;
    --wave-white: #f3f4f7;
    --teal: #1aa59a;
  }
  * { margin: 0; padding: 0; box-sizing: border-box; }
  html, body { width: 1200px; height: 750px; overflow: hidden; background: var(--bg); }
  .canvas { position: relative; width: 1200px; height: 750px; }

  .panel { position: absolute; overflow: hidden; }
  .panel svg.panel-art { position: absolute; inset: 0; width: 100%; height: 100%; }
  .panel-top { left: 14px; top: 45px; width: 760px; height: 398px; }
  .panel-front { left: 14px; top: 451px; width: 760px; height: 253px; }
  .panel-end { left: 788px; top: 451px; width: 398px; height: 253px; background: var(--wave-white); }

  .brand { position: absolute; text-align: center; white-space: nowrap; }
  .brand-name {
    font-family: "Archivo Black", sans-serif;
    line-height: 1;
    color: var(--navy);
  }
  .brand-tagline {
    font-family: "Kaushan Script", cursive;
    color: var(--navy);
    line-height: 1.1;
  }
  .panel-top .brand { left: 190px; top: 92px; width: 380px; }
  .panel-top .brand-name { font-size: 92px; }
  .panel-top .brand-tagline { font-size: 24px; margin-top: 4px; }
  .panel-front .brand { left: 200px; top: 50px; width: 360px; }
  .panel-front .brand-name { font-size: 86px; }
  .panel-front .brand-tagline { font-size: 22px; margin-top: 4px; }
  .panel-end .brand { left: 0; top: 70px; width: 398px; }
  .panel-end .brand-name { font-size: 70px; }
  .panel-end .brand-tagline { font-size: 19px; margin-top: 4px; }

  .claim {
    position: absolute;
    left: 26px; top: 24px;
    font-family: "Arimo", sans-serif;
    font-size: 12px;
    line-height: 1.1;
    color: var(--white);
    letter-spacing: 0.2px;
  }

  .pack-size {
    position: absolute;
    font-family: "Archivo Black", sans-serif;
    color: var(--navy);
    line-height: 1;
    text-align: center;
  }
  .pack-size .label { font-size: 18px; display: block; }
  .pack-size .count { font-size: 27px; display: block; margin-top: 2px; }
  .pack-size .ply { font-family: "Arimo", sans-serif; font-size: 13px; font-weight: 400; }
  .panel-top .pack-size { right: 30px; top: 190px; }
  .panel-front .pack-size { left: 26px; bottom: 20px; }

  .badge { position: absolute; }
  .panel-top .badge { left: 70px; top: 262px; width: 112px; height: 112px; }
  .panel-front .badge { right: 22px; top: 18px; width: 100px; height: 100px; }
</style>
</head>
<body>
<div class="canvas">

  <section class="panel panel-top" aria-label="Box top panel">
    <svg class="panel-art" viewBox="0 0 760 398" preserveAspectRatio="none">
      <defs>
        <radialGradient id="topBurst" cx="0.45" cy="0.4" r="0.7">
          <stop offset="0" stop-color="#6cc3ee"/>
          <stop offset="0.45" stop-color="#0a86d2"/>
          <stop offset="1" stop-color="#0567b5"/>
        </radialGradient>
      </defs>
      <rect width="760" height="398" fill="url(#topBurst)" role="img" aria-label="Blue light-ray burst background"/>
      <path d="M0,338 C220,308 430,188 760,63 L760,398 L0,398 Z" fill="#f3f4f7" role="img" aria-label="Soft white wave pattern"/>
      <path d="M0,330 C220,300 430,180 760,55" fill="none" stroke="#3aa7e0" stroke-width="16"/>
      <path d="M565,128 C630,102 695,74 760,42" fill="none" stroke="#26237e" stroke-width="11"/>
    </svg>

    <p class="claim">NON-LOTION WHITE FACIAL TISSUE<br>MOUCHOIRS BLANCS SANS LOTION</p>

    <div class="brand">
      <div class="brand-name">Velora</div>
      <div class="brand-tagline">Soft White Facial Tissues</div>
    </div>

    <div class="pack-size">
      <span class="label">White Tissues</span>
      <span class="count">150-2<span class="ply">PLY</span></span>
    </div>

    <svg class="badge" viewBox="0 0 112 112" role="img" aria-label="Dermatologist approval seal">
      <circle cx="56" cy="56" r="54" fill="#ffffff"/>
      <circle cx="56" cy="56" r="44" fill="none" stroke="#1aa59a" stroke-width="3"/>
      <circle cx="56" cy="56" r="26" fill="#1aa59a"/>
    </svg>
  </section>

  <section class="panel panel-front" aria-label="Box front panel">
    <svg class="panel-art" viewBox="0 0 760 253" preserveAspectRatio="none">
      <defs>
        <radialGradient id="frontBurst" cx="0.5" cy="0.45" r="0.65">
          <stop offset="0" stop-color="#7ccbf1"/>
          <stop offset="0.45" stop-color="#0a86d2"/>
          <stop offset="1" stop-color="#0567b5"/>
        </radialGradient>
      </defs>
      <rect width="760" height="253" fill="url(#frontBurst)" role="img" aria-label="Blue light-ray burst background"/>
    </svg>

    <div class="brand">
      <div class="brand-name">Velora</div>
      <div class="brand-tagline">Soft White Facial Tissues</div>
    </div>

    <div class="pack-size">
      <span class="label">White Tissues</span>
      <span class="count">150-2<span class="ply">PLY</span></span>
    </div>

    <svg class="badge" viewBox="0 0 112 112" role="img" aria-label="Dermatologist approval seal">
      <circle cx="56" cy="56" r="54" fill="#ffffff"/>
      <circle cx="56" cy="56" r="44" fill="none" stroke="#1aa59a" stroke-width="3"/>
      <circle cx="56" cy="56" r="26" fill="#1aa59a"/>
    </svg>
  </section>

  <section class="panel panel-end" aria-label="Box end panel">
    <svg class="panel-art" viewBox="0 0 398 253" preserveAspectRatio="none">
      <rect width="398" height="253" fill="#f3f4f7" role="img" aria-label="Soft white wave pattern"/>
    </svg>
    <div class="brand">
      <div class="brand-name">Velora</div>
      <div class="brand-tagline">Soft White Facial Tissues</div>
    </div>
  </section>

</div>
</body>
</html>
```